Halvorsen Partners Business Card

Halvorsen Partners Civil Construction
Marcus Halvorsen
CEO
727-518-6094
Marcus@HalvorsenSiteworks.example
www.HalvorsenSiteworks.example
Site Development
Utility Construction
Excavation
40876 County Lane 19
Land O' Lakes, FL 34638

Target Market(s)

Construction and government

Industry/Entity Type

Business

Contact Information for Business Card

I want an unique design that make a statement

Number of Pages Required

1 page

Font styles to use

Colors

Designer to choose colors to be used in the design.

Requirements
Must have
• unique design, feel free to modify or change the color of my logo.
Nice to have
• extra design features like spot UV, foil accents, color edges, unique paper, or any thing that would make my card pop.
• I like the feel of the image that I attached

```html
<!DOCTYPE html>
<html lang="en">
<head>
<meta charset="utf-8">
<title>Halvorsen Partners Business Card</title>
<link rel="stylesheet" href="https://fonts.googleapis.com/css2?family=Source+Sans+3:wght@400;600;700&display=swap">
<style>
  :root {
    --backdrop: #2b2c2e;
    --brand-blue: #1f3f8f;
    --card-white: #f7f7f6;
    --card-dark: #4a4b4d;
    --card-dark-edge: #3a3b3d;
    --ink-grey: #5b5d60;
    --ink-light: #e6e6e6;
    --muted-light: #b9babc;
  }
  * { box-sizing: border-box; margin: 0; padding: 0; }
  html, body {
    width: 1200px; height: 960px; overflow: hidden;
    background: var(--backdrop);
    font-family: "Source Sans 3", "Myriad Pro", sans-serif;
  }
  .stage {
    position: relative; width: 1200px; height: 960px;
  }
  .card {
    position: absolute; left: 250px; width: 700px; height: 400px;
    box-shadow: 0 10px 30px rgba(0,0,0,0.45);
    overflow: hidden;
  }

  /* Back side */
  .card-back {
    top: 50px;
    background: linear-gradient(135deg, var(--card-dark) 0%, var(--card-dark-edge) 100%);
    display: flex; flex-direction: column; align-items: center; justify-content: center;
  }
  .wordmark { display: flex; align-items: center; gap: 16px; }
  .wordmark-square {
    width: 56px; height: 56px; border: 4px solid currentColor;
  }
  .wordmark-divider { width: 2px; align-self: stretch; background: currentColor; opacity: .6; }
  .wordmark-text { display: flex; flex-direction: column; }
  .wordmark-name { font-weight: 600; font-size: 32px; letter-spacing: 1px; text-transform: uppercase; line-height: 1; }
  .wordmark-tag { font-weight: 400; font-size: 16px; letter-spacing: 5px; text-transform: uppercase; margin-top: 6px; }
  .card-back .wordmark { color: var(--ink-light); }
  .card-back .wordmark-tag { color: var(--muted-light); }
  .services {
    margin-top: 34px; display: flex; align-items: center; gap: 12px;
    color: var(--ink-light); font-size: 17px;
  }
  .services .dot { width: 7px; height: 7px; background: var(--ink-light); }

  /* Front side */
  .card-front {
    top: 500px; background: var(--card-white);
  }
  .front-band {
    position: absolute; left: 0; top: 0; width: 90px; height: 100%;
    background: var(--brand-blue);
  }
  .card-front .wordmark {
    position: absolute; left: 112px; top: 34px; gap: 12px;
  }
  .card-front .wordmark-square { width: 42px; height: 42px; border-width: 3px; color: var(--ink-grey); }
  .card-front .wordmark-divider { background: var(--ink-grey); width: 1px; }
  .card-front .wordmark-name { color: var(--brand-blue); font-size: 26px; }
  .card-front .wordmark-tag { color: var(--ink-grey); font-size: 13px; letter-spacing: 4px; }

  .contact {
    position: absolute; right: 34px; bottom: 30px; text-align: right;
  }
  .person-name { color: var(--brand-blue); font-weight: 700; font-size: 24px; letter-spacing: .5px; text-transform: uppercase; }
  .person-role { color: var(--ink-grey); font-size: 18px; margin-bottom: 12px; }
  .contact-line {
    display: flex; align-items: center; justify-content: flex-end; gap: 10px;
    color: var(--ink-grey); font-size: 17px; line-height: 25px;
  }
  .contact-line svg { width: 16px; height: 16px; fill: var(--brand-blue); flex: none; }
</style>
</head>
<body>
<main class="stage">

  <section class="card card-back" aria-label="Card back">
    <div class="wordmark">
      <span class="wordmark-square"></span>
      <span class="wordmark-divider"></span>
      <div class="wordmark-text">
        <span class="wordmark-name">Halvorsen Partners</span>
        <span class="wordmark-tag">Civil Construction</span>
      </div>
    </div>
    <div class="services">
      <span>Site Development</span><span class="dot"></span>
      <span>Utility Construction</span><span class="dot"></span>
      <span>Excavation</span>
    </div>
  </section>

  <section class="card card-front" aria-label="Card front">
    <div class="front-band"></div>
    <div class="wordmark">
      <span class="wordmark-square"></span>
      <span class="wordmark-divider"></span>
      <div class="wordmark-text">
        <span class="wordmark-name">Halvorsen Partners</span>
        <span class="wordmark-tag">Civil Construction</span>
      </div>
    </div>

    <div class="contact">
      <div class="person-name">Marcus Halvorsen</div>
      <div class="person-role">CEO</div>
      <div class="contact-line">727-518-6094
        <svg viewBox="0 0 16 16" aria-hidden="true"><path d="M2 6c0-2 3-4 6-4s6 2 6 4v1h-3.5V5.5h-5V7H2z"/><rect x="3" y="8" width="10" height="6" rx="1"/></svg>
      </div>
      <div class="contact-line">Marcus@HalvorsenSiteworks.example
        <svg viewBox="0 0 16 16" aria-hidden="true"><path d="M1 4h14v9H1z M2 5l6 4.5L14 5"/><path d="M1 4l7 5 7-5v9H1z"/></svg>
      </div>
      <div class="contact-line">www.HalvorsenSiteworks.example
        <svg viewBox="0 0 16 16" aria-hidden="true"><circle cx="8" cy="8" r="7"/><path d="M3 8h10M8 2v12" stroke="#f7f7f6" stroke-width="1.2" fill="none"/></svg>
      </div>
    </div>
  </section>

</main>
</body>
</html>
```